PowerPoint Template Design

We are an independent private equity and advisory firm (mergers and acquisitions), based in Brazil. We are looking for a power point template to use for companies presentations to investors and other targets (ie competitors).
Find attached the actual template that we use, we need something with this structure but more customized.

- Cover slide with our logo, project name and current date
- Index/Agenda slide
- Content slides
a. Slide with title, subtitle, text and footer. The footer should contain the page number, the person who we are sending to and the word "CONFIDENTIAL"
b. Slide with title, subtitle, text and pictures/charters/graphics
- Final slide with adress and contacts

We do not want something very colorful, we need something plain, simple but modern.

Target Market(s)

Investors, CEOs, CFOs, other advisory firms like DNTallis, DSRH, Almsbury, etc.

Industry/Entity Type

Equity

Requirements
Must have
• - the same colors used by our designer;
- one font only (Century Gothic);

```html
<!DOCTYPE html>
<html lang="en">
<head>
<meta charset="utf-8">
<title>Norvale Partners – Presentation Template</title>
<link href="https://fonts.googleapis.com/css2?family=Didact+Gothic&display=swap" rel="stylesheet">
<style>
  :root{
    --yellow:#fcd21c;
    --yellow-soft:#f9e36a;
    --row-grey:#e4e4e4;
    --ink:#1e1e1e;
    --ink-soft:#3a3a3a;
    --grey-light:#f3f3f3;
    --grey-mid:#bdbdbd;
    --grey-dark:#8e8e8e;
    --caption:#2a2a2a;
    --page:#ffffff;
    --font:"Didact Gothic", "Century Gothic", sans-serif;
  }
  *{box-sizing:border-box;margin:0;padding:0}
  html,body{width:1200px;height:1200px;overflow:hidden;background:var(--page)}
  body{font-family:var(--font);color:var(--ink);position:relative}

  .deck{position:absolute;inset:0;display:grid;grid-template-columns:570px 570px;grid-template-rows:385px 385px 385px;gap:11px 20px;padding:11px 20px}

  .slide{position:relative;overflow:hidden;background:linear-gradient(180deg,var(--grey-light) 0%,#d6d6d6 45%,var(--grey-dark) 100%);box-shadow:0 2px 8px rgba(0,0,0,.25)}

  .brand{font-family:var(--font);font-weight:400;color:var(--ink-soft);line-height:1;white-space:nowrap}

  .contact{position:absolute;display:flex;gap:10px;font-size:7px;line-height:1.35;color:var(--ink);white-space:nowrap}
  .contact .sep{border-left:1px solid var(--ink);padding-left:8px}

  /* Cover */
  .cover .brand{position:absolute;left:26px;top:70px;font-size:32px}
  .cover .band{position:absolute;left:0;right:0;top:176px;height:92px;background:var(--yellow)}
  .cover .project{position:absolute;left:22px;top:190px;font-size:29px;font-weight:400;color:var(--ink);white-space:nowrap}
  .cover .subtitle{position:absolute;left:100px;top:236px;font-size:15px;font-style:italic;color:var(--ink)}
  .cover .portrait{position:absolute;right:30px;top:10px;width:180px;height:375px;background:linear-gradient(180deg,#cfc28a 0%,#8a7a2a 40%,#2b2b2b 70%,#1a1a1a 100%)}
  .cover .contact{left:22px;bottom:14px}

  /* Titles */
  .slide-title{position:absolute;left:30px;top:22px;font-size:16px;font-weight:400}
  .slide-title em{display:block;font-size:10px}

  /* Table of contents */
  .toc table{position:absolute;left:60px;top:62px;width:450px;border-collapse:collapse;font-size:11px}
  .toc th{background:#fff;padding:8px;text-align:left;font-size:12px;font-weight:400}
  .toc td{padding:8px;border-top:1px solid #fff}
  .toc td:first-child{width:60px;text-align:center}
  .toc tbody tr:nth-child(odd) td{background:var(--yellow-soft)}
  .toc tbody tr:nth-child(even) td{background:var(--row-grey)}

  /* Footer */
  .footer-yellow{position:absolute;left:0;right:0;bottom:0;height:42px;background:var(--yellow)}
  .footer-yellow .contact{left:14px;top:8px}
  .footer-yellow .brand{position:absolute;right:0;bottom:0;width:130px;height:60px;background:var(--grey-mid);font-size:12px;display:flex;align-items:center;justify-content:center}

  /* Pictures */
  .formula{position:absolute;left:20px;top:24px;display:flex;align-items:center;gap:8px}
  .formula .box{width:110px;height:20px;background:#fff;border:1px solid #999;font-size:7px;display:flex;align-items:center;justify-content:center}
  .formula .plus{font-size:16px}
  .cards{position:absolute;left:20px;top:70px;display:flex;gap:16px}
  .card{width:165px}
  .card .cap{background:var(--caption);color:#fff;font-size:11px;text-align:center;padding:4px 0}
  .card .photo{height:130px}
  .photo-a{background:linear-gradient(135deg,#fafafa,#5a3a2a)}
  .photo-b{background:linear-gradient(135deg,#6a4a2a,#c2383a,#e0b040)}
  .photo-c{background:linear-gradient(135deg,#3a2a1a,#e6d2b0,#e07030)}

  /* Content with table */
  .data{position:absolute;left:140px;top:58px;width:300px;border-collapse:collapse;font-size:8px;text-align:center;box-shadow:0 1px 3px rgba(0,0,0,.3)}
  .data th{background:var(--row-grey);font-size:11px;font-weight:400;padding:6px 4px;border-right:1px solid #fff}
  .data td{padding:5px 4px;border-right:1px solid #fff}
  .data tbody tr:nth-child(odd) td{background:var(--yellow-soft)}
  .data tbody tr:nth-child(even) td{background:var(--row-grey)}
  .discover{position:absolute;left:18px;top:178px;font-size:12px;font-weight:400}
  .columns{position:absolute;left:18px;top:198px;right:18px;columns:3;column-gap:18px;font-size:6.5px;line-height:1.35}
  .columns p{text-indent:8px}

  /* Back cover */
  .back{background:linear-gradient(180deg,#e8e8e8,#b8b8b8)}
  .back .portrait{position:absolute;left:0;top:0;width:150px;height:100%;background:linear-gradient(180deg,#d9c36a 0%,#c59a3a 50%,#6a5a2a 100%)}
  .back .brand{position:absolute;left:150px;right:0;top:80px;text-align:center;font-size:30px}
  .back .thanks{position:absolute;left:150px;right:0;top:170px;text-align:center;font-size:26px;color:var(--ink-soft)}
  .back .contact{left:230px;bottom:12px}

  /* Bullets */
  .bullets{position:absolute;left:30px;top:70px;right:30px}
  .bullet-row{display:flex;gap:16px;align-items:center;padding:10px 0;border-bottom:1px solid #777}
  .bullet-row:last-child{border-bottom:0}
  .bullet-label{width:120px;font-size:12px;display:flex;align-items:center;gap:6px}
  .bullet-label .dot{width:12px;height:12px;background:var(--ink-soft)}
  .bullet-row ul{list-style:none;font-size:8.5px;line-height:1.55}
  .bullets-slide .footer-yellow{height:30px}
  .bullets-slide .footer-yellow .contact{top:5px}
</style>
</head>
<body>
<main class="deck">

  <section class="slide cover">
    <div class="brand">Norvale Partners</div>
    <div class="band"></div>
    <h1 class="project">Project Name Goes Here</h1>
    <p class="subtitle">Project Subtitle Goes Here</p>
    <div class="portrait" role="img" aria-label="Portrait photo of a businessman in a dark suit"></div>
    <div class="contact">
      <span>Rua Aurora, 410 – Centro<br>Porto Claro | Brazil</span>
      <span class="sep">+00 0 000 0000<br>Mobile +00 0 000 0001</span>
      <span class="sep">www.norvale.example</span>
    </div>
  </section>

  <section class="slide toc">
    <h2 class="slide-title">Table of Contents</h2>
    <table>
      <thead><tr><th>Slide</th><th>Slide Name</th></tr></thead>
      <tbody>
        <tr><td>1</td><td>Cover</td></tr>
        <tr><td>2</td><td>Table of Contents</td></tr>
        <tr><td>3</td><td>Content Slide with Table</td></tr>
        <tr><td>4</td><td>Content Slide with Pictures</td></tr>
        <tr><td>5</td><td>Content Slide with Bullet Points</td></tr>
        <tr><td>6</td><td>Back Cover</td></tr>
      </tbody>
    </table>
    <div class="footer-yellow">
      <div class="contact">
        <span>Rua Aurora, 410 – Centro<br>Porto Claro | Brazil<br>www.norvale.example</span>
        <span class="sep">+00 0 000 0000<br>Mobile +00 0 000 0001</span>
      </div>
    </div>
  </section>

  <section class="slide pictures">
    <div class="formula">
      <span class="box">xxxx</span><span class="plus">+</span>
      <span class="box">xxxx</span><span class="plus">+</span>
      <span class="box">xxxx</span><span class="plus">+</span>
    </div>
    <div class="cards">
      <figure class="card"><figcaption class="cap">Text Here</figcaption><div class="photo photo-a" role="img" aria-label="Photo of a chocolate dessert on a plate"></div></figure>
      <figure class="card"><figcaption class="cap">Text Here</figcaption><div class="photo photo-b" role="img" aria-label="Photo of sliced meat with vegetables"></div></figure>
      <figure class="card"><figcaption class="cap">Text Here</figcaption><div class="photo photo-c" role="img" aria-label="Photo of a plated seafood dish"></div></figure>
    </div>
    <div class="footer-yellow">
      <div class="contact">
        <span>Rua Aurora, 410 – Centro<br>Porto Claro | Brazil<br>www.norvale.example</span>
        <span class="sep">+00 0 000 0000<br>Mobile +00 0 000 0001</span>
      </div>
      <div class="brand">Norvale Partners</div>
    </div>
  </section>

  <section class="slide content-table">
    <h2 class="slide-title">Content Slide<em>with Table</em></h2>
    <table class="data">
      <thead><tr><th>Service</th><th>Time</th><th>Savings</th></tr></thead>
      <tbody>
        <tr><td>Service A</td><td>1 Month</td><td>10%</td></tr>
        <tr><td>Service B</td><td>4 Months</td><td>25%</td></tr>
        <tr><td>Service C</td><td>8 Months</td><td>45%</td></tr>
        <tr><td>Service D</td><td>12 Months</td><td>70%</td></tr>
      </tbody>
    </table>
    <h3 class="discover">Discover what we can do for your business</h3>
    <div class="columns">
      <p>"Lorem ipsum dolor sit amet, consectetur adipisicing elit, sed do eiusmod tempor incididunt ut labore et dolore magna aliqua. Ut enim ad minim veniam, quis nostrud exercitation ullamco laboris nisi ut aliquip ex ea commodo consequat. Duis aute irure dolor in reprehenderit in voluptate velit esse cillum dolore eu fugiat nulla pariatur. Excepteur sint occaecat cupidatat non proident, sunt in culpa qui officia deserunt mollit anim id est laborum.</p>
      <p>Lorem ipsum dolor sit amet, consectetur adipisicing elit, sed do eiusmod tempor incididunt ut labore et dolore magna aliqua. Ut enim ad minim veniam, quis nostrud exercitation ullamco laboris nisi ut aliquip ex ea commodo consequat. Duis aute irure dolor in reprehenderit in voluptate velit esse cillum dolore eu fugiat nulla pariatur. Excepteur sint occaecat cupidatat non proident, sunt in culpa qui officia deserunt mollit anim id est laborum.</p>
      <p>Lorem ipsum dolor sit amet, consectetur adipisicing elit, sed do eiusmod tempor incididunt ut labore et dolore magna aliqua. Ut enim ad minim veniam, quis nostrud exercitation ullamco laboris nisi ut aliquip ex ea commodo consequat. Duis aute irure dolor in reprehenderit in voluptate velit esse cillum dolore eu fugiat nulla pariatur. Excepteur sint occaecat cupidatat non proident, sunt in culpa qui officia deserunt mollit anim id est laborum."</p>
    </div>
    <div class="footer-yellow">
      <div class="contact">
        <span>Rua Aurora, 410 – Centro<br>Porto Claro | Brazil<br>www.norvale.example</span>
        <span class="sep">+00 0 000 0000<br>Mobile +00 0 000 0001</span>
      </div>
      <div class="brand">Norvale Partners</div>
    </div>
  </section>

  <section class="slide back">
    <div class="portrait" role="img" aria-label="Portrait photo of a smiling businessman"></div>
    <div class="brand">Norvale Partners</div>
    <p class="thanks">Thank You</p>
    <div class="contact">
      <span>Rua Aurora, 410 – Centro<br>Porto Claro | Brazil</span>
      <span class="sep">+00 0 000 0000<br>Mobile +00 0 000 0001</span>
    </div>
  </section>

  <section class="slide bullets-slide">
    <h2 class="slide-title">Content Slide<em>with Bullet Points</em></h2>
    <div class="bullets">
      <div class="bullet-row">
        <div class="bullet-label"><span class="dot"></span>Bullet Point #1</div>
        <ul><li>Lorem ipsum dolor sit amet, consectetur adipisicing elit</li><li>Sed do eiusmod tempor incididunt ut labore et dolore magna aliqua</li><li>Duis aute irure dolor in reprehenderit in voluptate velit esse</li><li>Lorem ipsum dolor sit amet, consectetur adipisicing</li></ul>
      </div>
      <div class="bullet-row">
        <div class="bullet-label"><span class="dot"></span>Bullet Point #2</div>
        <ul><li>Lorem ipsum dolor sit amet, consectetur adipisicing elit</li><li>Sed do eiusmod tempor incididunt ut labore et dolore magna aliqua</li><li>Duis aute irure dolor in reprehenderit in voluptate velit esse</li><li>Lorem ipsum dolor sit amet, consectetur adipisicing</li></ul>
      </div>
      <div class="bullet-row">
        <div class="bullet-label"><span class="dot"></span>Bullet Point #3</div>
        <ul><li>Lorem ipsum dolor sit amet, consectetur adipisicing elit</li><li>Sed do eiusmod tempor incididunt ut labore et dolore magna aliqua</li><li>Duis aute irure dolor in reprehenderit in voluptate velit esse</li><li>Lorem ipsum dolor sit amet, consectetur adipisicing</li></ul>
      </div>
    </div>
    <div class="footer-yellow">
      <div class="contact">
        <span>Rua Aurora, 410 – Centro<br>Porto Claro | Brazil</span>
        <span class="sep">+00 0 000 0000<br>Mobile +00 0 000 0001</span>
      </div>
    </div>
  </section>

</main>
</body>
</html>
```